Mini Market Tolvo Business Presentation Cards

We need presentation cards with a logo we already own designed at this website as well. We need the printing, delivery and sleek, modem design in harmony with our previous logo design.

Target Market(s)

Low, med and High income class.

Industry/Entity Type

Grocery Store

Contact Information for Business Card

Business logo (Mini Market Tolvo), name: Esteban L. Morales/Lidia E. Paredes/ Iván Paredes (those are the names for the different cards),
Address: Col. Lomas del Valle, carretera a Tegel a 150mts del Centro Vial. Villa Serena, Costa Norte.
Email: minimarkettolvo@correofalso.hn
Teléfono: (504) 9715-3068

Font styles to use
Serif
Sans Serif

Requirements
Must have
• Business logo (Mini Market Tolvo), person name, department,
• Address, phone number, email address.

```html
<!DOCTYPE html>
<html lang="es">
<head>
<meta charset="utf-8">
<title>Mini Market Tolvo — Tarjetas de presentación</title>
<link rel="stylesheet" href="https://fonts.googleapis.com/css2?family=Tinos:wght@400;700&display=swap">
<style>
  :root{
    --bg:#e8e5df;
    --card:#ffffff;
    --green:#8cc63f;
    --green-dark:#76b02e;
    --red:#e4532e;
    --ink:#1e1e1e;
    --faint-green:#eef4e6;
  }
  *{box-sizing:border-box;margin:0;padding:0}
  html,body{width:1200px;height:780px;overflow:hidden}
  body{background:var(--bg);font-family:"Tinos","Times New Roman",serif;color:var(--ink);position:relative}

  .card{position:absolute;left:320px;width:560px;height:320px;background:var(--card);
        overflow:hidden;box-shadow:0 6px 18px rgba(0,0,0,.18)}
  .card--front{top:48px}
  .card--back{top:412px}

  /* front */
  .front-band{position:absolute;right:0;top:0;width:92px;height:100%;
              background:linear-gradient(180deg,var(--green),var(--green-dark))}
  .front-watermark{position:absolute;left:-70px;top:150px;width:260px;height:260px;border-radius:50%;
                   background:var(--faint-green)}
  .brand-disc{position:absolute;border-radius:50%;background:var(--green);border:5px solid #fff;
              box-shadow:0 0 0 2px rgba(0,0,0,.05)}
  .card--front .brand-disc{right:38px;top:22px;width:108px;height:108px}
  .brand-name{position:absolute;color:var(--red);font-weight:400;line-height:1;text-align:center}
  .brand-name .line-small{display:block;font-size:24px;letter-spacing:.5px}
  .brand-name .line-large{display:block;font-size:56px;margin-top:2px}
  .card--front .brand-name{left:180px;top:40px;width:230px}

  .person{position:absolute;left:40px;top:176px}
  .person-name{color:var(--red);font-size:20px;letter-spacing:.5px;text-transform:uppercase}
  .person-role{font-size:17px;margin-top:2px}

  .address{position:absolute;left:290px;top:178px;width:170px;font-size:14px;line-height:1.45;font-style:normal}

  .contact{position:absolute;left:40px;top:244px;font-size:15px;line-height:1}
  .contact-row{display:flex;align-items:center;gap:10px;margin-bottom:10px}
  .contact-icon{width:22px;height:22px;background:var(--green);display:flex;align-items:center;justify-content:center;flex:none}

  /* back */
  .back-band{position:absolute;left:0;bottom:0;width:100%;height:118px;
             background:linear-gradient(180deg,var(--green),var(--green-dark))}
  .card--back .brand-disc{right:60px;top:120px;width:130px;height:130px}
  .card--back .brand-name{left:90px;top:80px;width:280px}
  .card--back .brand-name .line-small{font-size:28px}
  .card--back .brand-name .line-large{font-size:64px}
</style>
</head>
<body>

<section class="card card--front" aria-label="Frente de la tarjeta">
  <div class="front-watermark" role="img" aria-label="Marca decorativa tenue de la tienda"></div>
  <div class="front-band"></div>
  <div class="brand-disc"></div>
  <h1 class="brand-name"><span class="line-small">Mini Market</span><span class="line-large">Tolvo</span></h1>

  <div class="person">
    <p class="person-name">Esteban L. Morales</p>
    <p class="person-role">Gerente Administrativo</p>
  </div>

  <address class="address">
    Col. Lomas del Valle, calle al Mirador, frente al Centro Vial.<br>
    Villa Serena, Costa Norte.
  </address>

  <div class="contact">
    <div class="contact-row">
      <span class="contact-icon">
        <svg width="14" height="14" viewBox="0 0 24 24" aria-hidden="true"><path fill="#fff" d="M6.6 10.8a15.1 15.1 0 0 0 6.6 6.6l2.2-2.2c.3-.3.7-.4 1-.2 1.1.4 2.3.6 3.6.6.6 0 1 .4 1 1V20c0 .6-.4 1-1 1A17 17 0 0 1 3 4c0-.6.4-1 1-1h3.5c.6 0 1 .4 1 1 0 1.3.2 2.5.6 3.6.1.3 0 .7-.2 1z"/></svg>
      </span>
      <span>(504) 9715-3068</span>
    </div>
    <div class="contact-row">
      <span class="contact-icon">
        <svg width="14" height="12" viewBox="0 0 24 18" aria-hidden="true"><rect x="1" y="1" width="22" height="16" fill="none" stroke="#fff" stroke-width="2"/><path d="M1 1l11 9 11-9" fill="none" stroke="#fff" stroke-width="2"/></svg>
      </span>
      <span>minimarkettolvo@correofalso.hn</span>
    </div>
  </div>
</section>

<section class="card card--back" aria-label="Reverso de la tarjeta">
  <div class="back-band"></div>
  <h2 class="brand-name"><span class="line-small">Mini Market</span><span class="line-large">Tolvo</span></h2>
  <div class="brand-disc"></div>
</section>

</body>
</html>
```